SeniorPlum needs a new packaging

We are Coffee Roasters based in Versailles France.

We want a new design for our coffee packaging. The packaging is a basic brown paper bag. We are sticking on it a 99.1mm x 67.7mm Label.

We want a new design for the label. The label should have the following info : Name of the coffee, origin, one line of description, our website www.seniorplum.fr.

Enclosed you will find our logo, as well as a picture of our current packaging

The Design should be "simple yet sophisticate".

```html
<!DOCTYPE html>
<html lang="fr">
<head>
<meta charset="utf-8">
<title>SeniorPlum – Nº5 label</title>
<link rel="stylesheet" href="https://fonts.googleapis.com/css2?family=Open+Sans:ital,wght@0,400;0,600;1,600&display=swap">
<style>
  :root {
    --page: #ffffff;
    --paper-light: #f1dcae;
    --paper-mid: #c98f4c;
    --paper-dark: #6b3a14;
    --ink: #1b120a;
    --band: #000000;
    --band-text: #ffffff;
  }
  * { margin: 0; padding: 0; box-sizing: border-box; }
  html, body {
    width: 1200px; height: 1000px; overflow: hidden;
    background: var(--page);
  }
  .label {
    position: absolute; left: 100px; top: 158px;
    width: 1000px; height: 683px;
    overflow: hidden;
    color: var(--ink);
    font-family: "Open Sans", Arial, sans-serif;
    background:
      radial-gradient(ellipse 55% 60% at 32% 28%, var(--paper-light) 0%, rgba(241,220,174,0) 70%),
      radial-gradient(ellipse 80% 90% at 50% 50%, var(--paper-mid) 30%, var(--paper-dark) 100%);
  }
  .label__mark {
    position: absolute; left: 178px; top: 78px;
    width: 112px; height: 112px; border-radius: 50%;
    background: var(--ink);
  }
  .label__brand {
    position: absolute; left: 322px; top: 58px;
    font-weight: 400; font-size: 86px; line-height: 1.2;
    color: var(--ink);
  }
  .label__tagline {
    position: absolute; left: 328px; top: 172px;
    font-weight: 400; font-size: 30px;
  }
  .label__band {
    position: absolute; left: 0; top: 243px;
    width: 100%; height: 107px;
    background: var(--band); color: var(--band-text);
    font-size: 82px; line-height: 107px; text-align: center;
    letter-spacing: -1px;
  }
  .label__origin {
    position: absolute; left: 0; top: 360px; width: 100%;
    text-align: center; font-size: 39px; line-height: 49px;
  }
  .label__description {
    position: absolute; left: 0; top: 482px; width: 100%;
    text-align: center; font-size: 25px; font-style: italic; font-weight: 600;
  }
  .label__contact {
    position: absolute; left: 0; top: 570px; width: 100%;
    text-align: center; font-size: 23px; line-height: 34px; font-weight: 600;
  }
</style>
</head>
<body>
  <div class="label">
    <div class="label__mark"></div>
    <div class="label__brand">SeniorPlum</div>
    <div class="label__tagline">Artisan Torréfacteur</div>
    <div class="label__band">Nº5 de SeniorPlum</div>
    <div class="label__origin">100% Arabica<br>(Brésil, Congo, Ethiopie)</div>
    <div class="label__description">Description placed here</div>
    <div class="label__contact">14 rue des Tilleuls 78000 Versailles &nbsp;|&nbsp; Tel. +33 1 30 21 48 72<br>www.seniorplum.fr</div>
  </div>
</body>
</html>
```